Realty Group Needs Classy, Contemporary Letterhead Design

We need a letterhead design for a new realty company located in NY, USA. We buy investment properties to rehabilitate and or keep in our rental portfolio.

```html
<!DOCTYPE html>
<html lang="en">
<head>
<meta charset="utf-8">
<title>Meridian Realty Group – Letterhead</title>
<link href="https://fonts.googleapis.com/css2?family=Questrial&display=swap" rel="stylesheet">
<style>
  :root {
    --brand-purple: #4f2a93;
    --ink: #2a2a2a;
    --paper: #ffffff;
    --backdrop: #f2f2f2;
    --signature-tone: #d9d9dc;
  }
  * { margin: 0; padding: 0; box-sizing: border-box; }
  html, body {
    width: 1200px; height: 2400px; overflow: hidden;
    background: var(--backdrop);
    font-family: "Questrial", sans-serif;
  }
  .letterhead {
    position: absolute; left: 100px; top: 493px;
    width: 1000px; height: 1413px;
    background: var(--paper);
    box-shadow: 0 8px 30px rgba(0,0,0,0.12);
    overflow: hidden;
  }
  .letterhead__bands { position: absolute; inset: 0; }
  .brand {
    position: absolute; left: 71px; top: 78px;
    color: var(--brand-purple);
  }
  .brand__name { font-size: 54px; line-height: 1; letter-spacing: 1px; }
  .brand__tagline { font-size: 21px; margin-top: 6px; letter-spacing: 1.5px; padding-left: 86px; }
  .contact {
    position: absolute; left: 662px; top: 36px;
    list-style: none; color: #fff; font-size: 20px; line-height: 24.5px;
  }
  .contact li { display: flex; align-items: center; gap: 12px; }
  .contact svg { width: 18px; height: 18px; flex: none; }
  .letter {
    position: absolute; left: 71px; top: 328px; width: 848px;
    color: var(--ink);
  }
  .letter__salutation { font-size: 24px; margin: 0 0 14px 4px; }
  .letter__paragraph {
    font-size: 15.6px; line-height: 20.2px; text-align: justify;
    margin-bottom: 20px;
  }
  .signature {
    position: absolute; left: 71px; top: 1136px;
    width: 180px; height: 100px;
    background: linear-gradient(135deg, var(--signature-tone), #ececef);
    border-radius: 4px;
  }
</style>
</head>
<body>
  <main class="letterhead">
    <svg class="letterhead__bands" viewBox="0 0 1000 1413" width="1000" height="1413" aria-hidden="true">
      <path fill="var(--brand-purple)" d="M0 0 H1000 V150 H600 C560 150 548 138 533 105 C518 65 500 40 455 40 H0 Z"/>
      <path fill="var(--brand-purple)" d="M0 1387 H298 C316 1387 322 1395 330 1402 H1000 V1413 H0 Z"/>
    </svg>

    <header class="brand">
      <div class="brand__name">MERIDIAN</div>
      <div class="brand__tagline">Realty Group, LLC</div>
    </header>

    <ul class="contact">
      <li>
        <svg viewBox="0 0 24 24"><path fill="none" stroke="#fff" stroke-width="2" d="M5 3h4l2 5-2.5 1.5a11 11 0 0 0 6 6L16 13l5 2v4a2 2 0 0 1-2 2A16 16 0 0 1 3 5a2 2 0 0 1 2-2z"/></svg>
        212-555-0147
      </li>
      <li>
        <svg viewBox="0 0 24 24"><rect x="3" y="6" width="18" height="13" rx="1" fill="none" stroke="#fff" stroke-width="2"/><path d="M3 7l9 7 9-7" fill="none" stroke="#fff" stroke-width="2"/></svg>
        info@meridianrealtyny.com
      </li>
      <li>
        <svg viewBox="0 0 24 24"><circle cx="12" cy="12" r="9" fill="none" stroke="#fff" stroke-width="2"/><path d="M3 12h18M12 3c3 3 3 15 0 18M12 3c-3 3-3 15 0 18" fill="none" stroke="#fff" stroke-width="1.6"/></svg>
        www.meridianrealtyny.com
      </li>
    </ul>

    <article class="letter">
      <p class="letter__salutation">Dear Sir,</p>
      <p class="letter__paragraph">Quis ipsum suspendisse ultrices gravida. Risus commodo viverra maecenas accumsan lacus vel facilisis. Lorem ipsum dolor sit amet, consectetur adipiscing elit, sed do eiusmod tempor incididunt ut labore et dolore magna aliqua. Quis ipsum suspendisse ultrices gravida. Risus commodo viverra maecenas accumsan lacus vel facilisis. Lorem ipsum dolor sit amet, consectetur adipiscing elit, sed do eiusmod tempor incididunt ut labore et dolore magna aliqua. Quis ipsum suspendisse ultrices gravida. Risus commodo viverra maecenas accumsan lacus vel facilisis. Lorem ipsum dolor sit amet, consectetur adipiscing elit, sed do eiusmod tempor incididunt ut labore et dolore magna aliqua. Quis ipsum suspendisse ultrices gravida. Risus commodo viverra maecenas accumsan lacus vel facilisis.</p>
      <p class="letter__paragraph">Lorem ipsum dolor sit amet, consectetur adipiscing elit, sed do eiusmod tempor incididunt ut labore et dolore magna aliqua. Quis ipsum suspendisse ultrices gravida. Risus commodo viverra maecenas accumsan lacus vel facilisis. Lorem ipsum dolor sit amet, consectetur adipiscing elit, sed do eiusmod tempor incididunt ut labore et dolore magna aliqua. Quis ipsum suspendisse ultrices gravida. Risus commodo viverra maecenas accumsan lacus vel facilisis. Lorem ipsum dolor sit amet, consectetur adipiscing elit, sed do eiusmod tempor incididunt ut labore et dolore magna aliqua. Quis ipsum suspendisse ultrices gravida. Risus commodo viverra maecenas accumsan lacus vel facilisis. Lorem ipsum dolor sit amet, consectetur adipiscing elit, sed do eiusmod tempor incididunt ut labore et dolore magna aliqua. Quis ipsum suspendisse ultrices gravida. Risus commodo viverra maecenas accumsan lacus vel facilisis.</p>
      <p class="letter__paragraph">Lorem ipsum dolor sit amet, consectetur adipiscing elit, sed do eiusmod tempor incididunt ut labore et dolore magna aliqua. Quis ipsum suspendisse ultrices gravida. Risus commodo viverra maecenas accumsan lacus vel facilisis. Lorem ipsum dolor sit amet, consectetur adipiscing elit, sed do eiusmod tempor incididunt ut labore et dolore magna aliqua. Quis ipsum suspendisse ultrices gravida. Risus commodo viverra maecenas accumsan lacus vel facilisis. Lorem ipsum dolor sit amet, consectetur adipiscing elit, sed do eiusmod tempor incididunt ut labore et dolore magna aliqua. Quis ipsum suspendisse ultrices gravida. Risus commodo viverra maecenas accumsan lacus vel facilisis. Lorem ipsum dolor sit amet, consectetur adipiscing elit, sed do eiusmod tempor incididunt ut labore et dolore magna aliqua. Quis ipsum suspendisse ultrices gravida. Risus commodo viverra maecenas accumsan lacus vel facilisis. Lorem ipsum dolor sit amet, consectetur adipiscing elit, sed do eiusmod tempor incididunt ut labore et dolore magna aliqua. Quis ipsum suspendisse ultrices gravida. Risus commodo viverra maecenas accumsan lacus vel facilisis. Lorem ipsum dolor sit amet, consectetur adipiscing elit, sed do eiusmod tempor incididunt ut labore et dolore magna aliqua. Quis ipsum suspendisse ultrices gravida. Risus commodo viverra maecenas accumsan lacus vel facilisis.</p>
    </article>

    <div class="signature" role="img" aria-label="Handwritten signature of the sender"></div>
  </main>
</body>
</html>
```